Rack Card for Charter Sail Boat business in SF Bay

We are in need of a rack card design to highlight the business to tourists and locals. 2 sided card 3.86" x 8.39" (full bleed)

We are looking for visually appleaing designs on the front and back but a little more detail on the back.

Use the info provided (text and info) on the website to include the 3 key services (Quick, 1/2 day, fullday) and aspects of the boat, location and other key info for customers (not prices). DO NOT INCLUDE ALL THIS TEXT please pick the elements you would like to fit your design and inform the customer as you would like about the business.

I can also provide photos directly from the video if you think those would fit your design. If video doesn't work on this upload you can view it at the website or facebook page (www.fb.com/tidewrenllc)

Now included a few video pictures in files for your use

Target Market(s)

Tourists and locals to san francisco east bay. 25 - 55 years old. Men and women.

Industry/Entity Type

Entertainment

Colors
0455a3
ec1f27
f3f1f8

Requirements
Must have
• Highlight services, key contact information (email, phone, website site), Visual impact
• 2-sided card - 3.86" x 8.39" (98 x 213 mm)
Nice to have
• facebook link, electric engine(green),

```html
<!DOCTYPE html>
<html lang="en">
<head>
<meta charset="utf-8">
<title>Sail Tidewren Rack Card</title>
<link rel="stylesheet" href="https://fonts.googleapis.com/css2?family=Arvo:wght@400;700&family=Open+Sans:wght@400;600;700&display=swap">
<style>
  :root{
    --blue:#0455a3;
    --blue-deep:#03407d;
    --blue-light:#1c74c4;
    --red:#ec1f27;
    --red-deep:#c4161d;
    --paper:#f3f1f8;
    --white:#ffffff;
    --stage:#e4e5e8;
    --slab:'Arvo', serif;
    --sans:'Open Sans', sans-serif;
  }
  *{box-sizing:border-box;margin:0;padding:0}
  html,body{width:1182px;height:1200px;overflow:hidden;background:var(--stage)}
  .stage{position:relative;width:1182px;height:1200px}
  .card{position:absolute;top:93px;width:442px;height:953px;overflow:hidden;background:var(--white);
        box-shadow:0 4px 14px rgba(0,0,0,.25)}
  .card--front{left:106px}
  .card--back{left:610px}
  .card-bg{position:absolute;inset:0;width:442px;height:953px}
  .abs{position:absolute}

  .badge{left:17px;top:17px;width:77px;height:77px;border-radius:50%;background:var(--blue-deep);border:4px solid #d9b44a}
  .brand{display:flex;align-items:center;gap:8px;font-family:var(--slab);font-weight:400;color:var(--white);white-space:nowrap}
  .brand-dot{width:24px;height:24px;border-radius:50%;background:var(--white);flex:none}
  .brand--front{left:222px;top:50px;font-size:30px}
  .brand--back{left:20px;top:290px;font-size:38px}

  .polaroid{background:var(--white);padding:7px 7px 14px;box-shadow:0 3px 8px rgba(0,0,0,.35)}
  .polaroid .shot{width:100%;height:100%}
  .pin{position:absolute;top:-4px;width:11px;height:11px;border-radius:50%;background:var(--red);box-shadow:0 1px 2px rgba(0,0,0,.4)}

  .headline{left:182px;top:423px;width:225px;font-family:var(--slab);font-weight:400;font-size:18px;line-height:27px;color:var(--white);white-space:nowrap}
  .headline span{display:block;text-align:center}
  .values{right:44px;top:490px;text-align:right;font-family:var(--slab);font-size:14px;line-height:20px;color:var(--red)}
  .values li{list-style:none}
  .values svg{width:12px;height:10px;margin-left:6px;vertical-align:middle}

  .lead{left:30px;top:570px;width:382px;text-align:center;font-family:var(--sans);font-size:15.5px;line-height:19px;color:var(--white)}
  .body{left:28px;top:656px;width:386px;text-align:justify;font-family:var(--sans);font-size:12.3px;line-height:17.4px;color:var(--white)}

  .cta{left:64px;top:841px;width:306px;height:40px;border-radius:20px;background:linear-gradient(var(--red),var(--red-deep));
       color:var(--white);font-family:var(--sans);font-weight:700;font-size:15px;display:flex;align-items:center;justify-content:center;
       box-shadow:0 3px 6px rgba(0,0,0,.3)}
  .contact{left:0;top:890px;width:442px;text-align:center;font-family:var(--slab);color:var(--red);font-size:14.5px;line-height:25px;white-space:nowrap}

  .values-line{left:17px;top:377px;font-family:var(--slab);font-size:14.5px;color:var(--red);white-space:nowrap}
  .tab{left:0;top:406px;width:240px;height:42px;border-radius:0 21px 21px 0;background:linear-gradient(var(--red),var(--red-deep));
       color:var(--white);font-family:var(--slab);font-weight:400;font-size:19px;display:flex;align-items:center;padding-left:18px;box-shadow:0 3px 6px rgba(0,0,0,.3);white-space:nowrap}
  .service{left:17px;font-family:var(--sans);color:var(--white)}
  .service h3{font-family:var(--slab);font-weight:400;font-size:18px;line-height:24px;margin-bottom:3px;white-space:nowrap}
  .service p{font-size:12px;line-height:15px}
  .service--blast{top:455px;width:262px}
  .service--half{top:556px;width:258px}
  .service--full{top:655px;width:400px}
  .service--custom{top:723px;width:405px}

  .route{width:96px;height:96px;border-radius:50%;border:4px solid var(--white);background:radial-gradient(#e7eef5,#b9cfe2);
         box-shadow:0 3px 7px rgba(0,0,0,.35)}
</style>
</head>
<body>
<main class="stage">

  <section class="card card--front">
    <svg class="card-bg" viewBox="0 0 442 953" aria-hidden="true">
      <defs>
        <linearGradient id="sunset" x1="0" y1="0" x2="0" y2="1">
          <stop offset="0" stop-color="#1d3a6a"/>
          <stop offset=".45" stop-color="#e3a24a"/>
          <stop offset=".6" stop-color="#3b4d66"/>
          <stop offset="1" stop-color="#1a2533"/>
        </linearGradient>
        <linearGradient id="bodyBlue" x1="0" y1="0" x2="0" y2="1">
          <stop offset="0" stop-color="#0a4fa0"/>
          <stop offset="1" stop-color="#0c63b8"/>
        </linearGradient>
      </defs>
      <rect width="442" height="440" fill="url(#sunset)" role="img" aria-label="Photo: sunset over the bay from the deck of the sailboat"/>
      <path d="M0 340 C140 290 260 410 442 360 L442 953 L0 953Z" fill="#d5dbe4"/>
      <path d="M0 354 C140 304 260 424 442 376 L442 953 L0 953Z" fill="url(#bodyBlue)"/>
      <path d="M0 814 C140 844 300 840 442 802 L442 953 L0 953Z" fill="var(--blue-light)" opacity=".6"/>
      <path d="M0 827 C140 857 300 852 442 816 L442 953 L0 953Z" fill="var(--white)"/>
    </svg>

    <div class="abs badge" role="img" aria-label="Licensed captain badge"></div>
    <div class="abs brand brand--front"><span class="brand-dot"></span>Tidewren</div>

    <figure class="abs polaroid" style="left:8px;top:332px;width:162px;height:112px;transform:rotate(-3deg)">
      <div class="shot" role="img" aria-label="Photo: the sailboat moored at the marina" style="background:linear-gradient(#b9c8d6,#4e5f70)"></div>
      <span class="pin" style="left:10px"></span>
    </figure>
    <figure class="abs polaroid" style="left:38px;top:420px;width:140px;height:136px;transform:rotate(-5deg)">
      <div class="shot" role="img" aria-label="Photo: children in life jackets aboard" style="background:linear-gradient(#8fb4d8,#3a4a5c)"></div>
      <span class="pin" style="right:10px"></span>
    </figure>

    <h1 class="abs headline"><span>ULTIMATE EAST BAY</span><span>SAILBOAT CHARTER</span></h1>
    <ul class="abs values">
      <li>Modern<svg viewBox="0 0 12 10"><path d="M1 5l3.5 3.5L11 1.5" fill="none" stroke="currentColor" stroke-width="2"/></svg></li>
      <li>Entertaining<svg viewBox="0 0 12 10"><path d="M1 5l3.5 3.5L11 1.5" fill="none" stroke="currentColor" stroke-width="2"/></svg></li>
      <li>Safe<svg viewBox="0 0 12 10"><path d="M1 5l3.5 3.5L11 1.5" fill="none" stroke="currentColor" stroke-width="2"/></svg></li>
    </ul>

    <p class="abs lead">Come enjoy an amazing experience aboard Tidewren and view San Francisco and the rest of the bay as so few are able to do.</p>
    <p class="abs body">Tidewren is a supreme blue-water cruising boat with all the modern safety, comfort and entertainment equipment you would expect. Your time aboard Tidewren is yours to enjoy and direct as you wish while we show you San Francisco Bay, the Golden Gate Bridge, Alcatraz, Treasure and Angel Islands and so much more. Come join us and share the wonders around San Francisco Bay with your friends and family. We love to show families how to sail and have great fun on the water while staying safe.</p>

    <div class="abs cta">NOW ACCEPTING BOOKINGS!</div>
    <div class="abs contact">
      <div>Call: (510) 555-SAIL (7245)</div>
      <div>Bookings@SailTidewren.com &nbsp;|&nbsp; www.sailtidewren.com</div>
    </div>
  </section>

  <section class="card card--back">
    <svg class="card-bg" viewBox="0 0 442 953" aria-hidden="true">
      <defs>
        <linearGradient id="bay" x1="0" y1="0" x2="0" y2="1">
          <stop offset="0" stop-color="#9ec3e8"/>
          <stop offset=".35" stop-color="#5f88b5"/>
          <stop offset=".5" stop-color="#2b5b93"/>
          <stop offset="1" stop-color="#1c3553"/>
        </linearGradient>
        <linearGradient id="backBlue" x1="0" y1="0" x2="0" y2="1">
          <stop offset="0" stop-color="#0a4fa0"/>
          <stop offset="1" stop-color="#0c63b8"/>
        </linearGradient>
      </defs>
      <rect width="442" height="300" fill="url(#bay)" role="img" aria-label="Photo: view forward over the bow across the bay"/>
      <path d="M0 238 C100 195 250 235 442 205 L442 953 L0 953Z" fill="#d5dbe4"/>
      <path d="M0 252 C100 210 250 250 442 220 L442 953 L0 953Z" fill="url(#backBlue)"/>
      <path d="M0 842 C140 872 300 868 442 830 L442 953 L0 953Z" fill="var(--blue-light)" opacity=".6"/>
      <path d="M0 855 C140 885 300 880 442 844 L442 953 L0 953Z" fill="var(--white)"/>
    </svg>

    <figure class="abs polaroid" style="left:304px;top:168px;width:134px;height:128px;transform:rotate(5deg)">
      <div class="shot" role="img" aria-label="Photo: the sailboat at its berth" style="background:linear-gradient(#a9c6e2,#2f3f52)"></div>
      <span class="pin" style="left:12px"></span>
    </figure>
    <figure class="abs polaroid" style="left:284px;top:300px;width:152px;height:160px;transform:rotate(-5deg)">
      <div class="shot" role="img" aria-label="Photo: deck and rigging under way" style="background:linear-gradient(#c6d2de,#44505e)"></div>
      <span class="pin" style="right:12px"></span>
    </figure>
    <figure class="abs polaroid" style="left:292px;top:466px;width:146px;height:176px;transform:rotate(10deg)">
      <div class="shot" role="img" aria-label="Photo: mainsail filled with wind" style="background:linear-gradient(#e3e6ea,#7c8793)"></div>
      <span class="pin" style="left:14px"></span>
    </figure>

    <div class="abs brand brand--back"><span class="brand-dot"></span>Tidewren</div>
    <div class="abs values-line">Modern • Entertaining • Safe</div>
    <h2 class="abs tab">SERVICES OFFERED</h2>

    <div class="abs service service--blast">
      <h3>2 HOUR BLAST</h3>
      <p>Could be a sunset sail, an early morning wake up cruise or a blast out into the bay anytime to find peace, fresh air and amazing views.</p>
    </div>
    <div class="abs service service--half">
      <h3>1/2 DAY FUN</h3>
      <p>A full morning, afternoon or evening out in the Bay seeing many of the main features and landmarks close to the Bay from the water. Actual duration 4-5 hours anchor.</p>
    </div>
    <div class="abs service service--full">
      <h3>FULL DAY ADVENTURE</h3>
      <p>The day includes a complete circuit of the Bay and lunch at anchor. Actual duration 7-8 hours</p>
    </div>
    <div class="abs service service--custom">
      <h3>CUSTOM CRUISES</h3>
      <p>If your looking for something a little different or to mix it up a bit, let us know and we can make it happen.</p>
    </div>

    <div class="abs route" style="left:50px;top:792px" role="img" aria-label="Map: 2 hour route around the bay"></div>
    <div class="abs route" style="left:171px;top:792px" role="img" aria-label="Map: half day route around the bay"></div>
    <div class="abs route" style="left:292px;top:792px" role="img" aria-label="Map: full day circuit of the bay"></div>

    <div class="abs contact">
      <div>Call: (510) 555-SAIL (7245)</div>
      <div>Bookings@SailTidewren.com &nbsp;|&nbsp; www.sailtidewren.com</div>
    </div>
  </section>

</main>
</body>
</html>
```